Poster for a vegan café with a funny message about the food served.

Design a poster with the text "Eating here was a big missed stake!" for a café at a meditation center (lunavardet.se).

```html
<!DOCTYPE html>
<html lang="en">
<head>
<meta charset="utf-8">
<title>Eating Here Was A Huge Missed Steak! – Café Poster</title>
<link rel="stylesheet" href="https://fonts.googleapis.com/css2?family=Archivo+Black&family=Saira+Semi+Condensed:wght@300&display=swap">
<style>
  :root {
    --page-bg: #e6e6e6;
    --poster-bg: #ffffff;
    --mist-blue: #c9d4dc;
    --slate-blue: #6e91a6;
    --pale-grey: #d0d3d0;
    --stone-grey: #979889;
    --sand: #e8ddb8;
    --ochre: #c9ad69;
    --caption-blue: #6e8fa3;
    --teapot-tone: #e3e7e3;
    --figure-tone: #f3edd8;
  }
  * { margin: 0; padding: 0; box-sizing: border-box; }
  html, body {
    width: 1200px;
    height: 900px;
    overflow: hidden;
    background: var(--page-bg);
  }
  .canvas {
    width: 1200px;
    height: 900px;
    display: flex;
    align-items: center;
    justify-content: center;
  }
  .poster {
    width: 611px;
    height: 861px;
    background: var(--poster-bg);
    overflow: hidden;
  }
  .poster svg { display: block; width: 100%; height: 100%; }
  .headline {
    font-family: "Archivo Black", "Arial Black", sans-serif;
    font-size: 232px;
  }
  .headline--eating { fill: var(--mist-blue); }
  .headline--here { fill: var(--slate-blue); }
  .headline--was { fill: var(--pale-grey); }
  .headline--huge { fill: var(--stone-grey); }
  .headline--missed { fill: var(--sand); }
  .headline--steak { fill: var(--ochre); }
  .caption {
    font-family: "Saira Semi Condensed", "Arial Narrow", sans-serif;
    font-weight: 300;
    font-size: 66px;
    fill: var(--caption-blue);
  }
  .art-teapot { fill: var(--teapot-tone); }
  .art-figure { fill: var(--figure-tone); }
</style>
</head>
<body>
<main class="canvas">
  <article class="poster">
    <svg viewBox="0 0 718 1012" xmlns="http://www.w3.org/2000/svg" preserveAspectRatio="none">
      <g class="headline-stack">
        <text class="headline headline--eating" x="3" y="170" textLength="617" lengthAdjust="spacingAndGlyphs">EATING</text>
        <text class="headline headline--here" x="3" y="337" textLength="423" lengthAdjust="spacingAndGlyphs">HERE</text>
        <text class="headline headline--was" x="3" y="504" textLength="403" lengthAdjust="spacingAndGlyphs">WAS</text>
        <text class="headline headline--huge" x="0" y="672" textLength="603" lengthAdjust="spacingAndGlyphs">A HUGE</text>
        <text class="headline headline--missed" x="3" y="842" textLength="682" lengthAdjust="spacingAndGlyphs">MISSED</text>
        <text class="headline headline--steak" x="0" y="1012" textLength="596" lengthAdjust="spacingAndGlyphs">STEAK!</text>
      </g>
      <g class="caption-stack">
        <text class="caption" x="433" y="227" textLength="202" lengthAdjust="spacingAndGlyphs">EATING</text>
        <text class="caption" x="433" y="280" textLength="148" lengthAdjust="spacingAndGlyphs">HERE</text>
        <text class="caption" x="433" y="334" textLength="142" lengthAdjust="spacingAndGlyphs">WAS</text>
        <text class="caption" x="433" y="390" textLength="220" lengthAdjust="spacingAndGlyphs">A HUGE</text>
        <text class="caption" x="433" y="444" textLength="220" lengthAdjust="spacingAndGlyphs">MISSED</text>
        <text class="caption" x="433" y="496" textLength="195" lengthAdjust="spacingAndGlyphs">STEAK!</text>
      </g>
      <rect class="art-teapot" x="593" y="234" width="108" height="102" rx="40" role="img" aria-label="Line drawing of a steaming teapot with a small cup"/>
      <rect class="art-figure" x="610" y="484" width="108" height="182" rx="46" role="img" aria-label="Line drawing of a meditating figure with a lotus"/>
    </svg>
  </article>
</main>
</body>
</html>
```